Moder Business Card Design for Renewables Business

Need a business card design for my business. We collect & repurpose spent coffee ground from cafes. The cards will be made from recycled paper. Needs to fit our corporate colour scheme of white, green & brown (see logo for colour codes). Eco friendly, modern, intresting & eye catching.
This card needs to convey the message of the business and fit into its mantra of eco-friendly, sustainable etc.

Target Market(s)

Cafe Owners, Coffee Drinkers, Recycling Companies, Farmers

Industry/Entity Type

Recycling

Contact Information for Business Card

Name; Peter Halloran
Phone; 0412 386 527
e-mail; info@lumatrove.com.au
website; www.lumatrove.com.au

Font styles to use
Sans Serif
Script

Colors

Designer to choose colors to be used in the design.

Requirements
Must have
• FRONT;
• Logo, Name (Peter Halloran), phone number, e-mail address, website
• BACK;
• On the back in cursive text; 'GIVING GROUNDS A SECOND LIFE'
• Small facebook & Instagram logos with text 'Lumatrove'
Should not have
• messy design

```html
<!DOCTYPE html>
<html lang="en">
<head>
<meta charset="utf-8">
<title>Lumatrove Business Card</title>
<link rel="stylesheet" href="https://fonts.googleapis.com/css2?family=Montserrat:wght@400;800&family=Open+Sans:wght@400&family=Sansita+Swashed:wght@600&display=swap">
<style>
  :root {
    --backdrop: #8c8c8a;
    --paper: #ebe7e1;
    --brown: #7b4a1d;
    --green: #6e9a48;
    --white: #ffffff;
  }
  * { margin: 0; padding: 0; box-sizing: border-box; }
  html, body { width: 1200px; height: 900px; overflow: hidden; }
  body {
    background: var(--backdrop);
    display: flex;
    align-items: center;
    justify-content: center;
    gap: 80px;
    font-family: "Open Sans", sans-serif;
    color: var(--brown);
  }
  .card {
    width: 380px;
    height: 665px;
    background: var(--paper);
    border-radius: 26px;
    box-shadow: 0 10px 30px rgba(0,0,0,0.25);
    display: flex;
    flex-direction: column;
    align-items: center;
    text-align: center;
  }
  .card-front { padding-top: 90px; }
  .holder-name {
    font-family: "Montserrat", sans-serif;
    font-weight: 800;
    font-size: 26px;
    letter-spacing: 0.5px;
  }
  .holder-role {
    font-family: "Montserrat", sans-serif;
    font-size: 16px;
    margin-top: 4px;
  }
  .brand {
    margin-top: 60px;
    display: flex;
    flex-direction: column;
    align-items: center;
    gap: 22px;
  }
  .brand-dot {
    width: 120px; height: 120px;
    border-radius: 50%;
    border: 7px solid var(--brown);
  }
  .brand-name {
    font-family: "Open Sans", sans-serif;
    font-size: 38px;
    color: var(--green);
    letter-spacing: 1px;
  }
  .contact-icons {
    display: flex;
    gap: 22px;
    margin-top: 34px;
  }
  .contact-icons svg { width: 32px; height: 32px; }
  .contact-list {
    margin-top: 34px;
    list-style: none;
    font-size: 20px;
    line-height: 1.65;
  }
  .dash {
    width: 26px; height: 3px;
    background: var(--brown);
    margin-top: 16px;
  }
  .card-back { justify-content: center; padding-bottom: 60px; }
  .tagline {
    font-family: "Sansita Swashed", cursive;
    font-weight: 600;
    font-size: 32px;
    line-height: 1.3;
  }
  .social-row {
    display: flex;
    gap: 10px;
    margin-top: 22px;
  }
  .social-dot {
    width: 18px; height: 18px;
    border-radius: 50%;
    background: var(--brown);
  }
  .social-handle {
    font-size: 15px;
    margin-top: 12px;
  }
</style>
</head>
<body>
  <section class="card card-front">
    <h1 class="holder-name">PETER HALLORAN</h1>
    <p class="holder-role">Managing Director</p>

    <div class="brand">
      <div class="brand-dot"></div>
      <div class="brand-name">LUMATROVE</div>
    </div>

    <div class="contact-icons">
      <svg viewBox="0 0 32 32" aria-label="Phone">
        <circle cx="16" cy="16" r="16" fill="var(--brown)"/>
        <path d="M11 9 l3 0 l1.5 4 l-2 1.5 a9 9 0 0 0 4 4 l1.5 -2 l4 1.5 l0 3 a2 2 0 0 1 -2 2 a13 13 0 0 1 -12 -12 a2 2 0 0 1 2 -2z" fill="var(--white)"/>
      </svg>
      <svg viewBox="0 0 32 32" aria-label="Email">
        <circle cx="16" cy="16" r="16" fill="var(--brown)"/>
        <rect x="8" y="11" width="16" height="11" fill="none" stroke="var(--white)" stroke-width="1.8"/>
        <path d="M8 11 l8 6 l8 -6" fill="none" stroke="var(--white)" stroke-width="1.8"/>
      </svg>
      <svg viewBox="0 0 32 32" aria-label="Website">
        <circle cx="16" cy="16" r="16" fill="var(--brown)"/>
        <rect x="11" y="8" width="6" height="10" rx="3" fill="none" stroke="var(--white)" stroke-width="1.8" transform="rotate(20 14 13)"/>
        <rect x="15" y="14" width="6" height="10" rx="3" fill="none" stroke="var(--white)" stroke-width="1.8" transform="rotate(20 18 19)"/>
      </svg>
    </div>

    <ul class="contact-list">
      <li>0412 386 527</li>
      <li>info@lumatrove.com.au</li>
      <li>lumatrove.com.au</li>
    </ul>
    <div class="dash"></div>
  </section>

  <section class="card card-back">
    <p class="tagline">Giving Grounds<br>A Second<br>Life</p>
    <div class="dash"></div>
    <div class="social-row">
      <span class="social-dot"></span>
      <span class="social-dot"></span>
    </div>
    <p class="social-handle">Lumatrove</p>
  </section>
</body>
</html>
```